American Ingenuity + Italian Design = RTB
International consulting services from fine arts/advertising/construction & special events. A new company that will find the right connections to get your job done.

Card should include -
1. Company Name with logo: rosalind tavera Enterprises LLC
2. Address: 218 Marlow Bend, Highland Springs, VA 23091
3. Phone Number: 804.555.2164 (US)
4. Tagline: American Ingenuity + Italian Style + RTB (you can improve on this idea)
5. web address to be added eventually

Likes: airplanes and boats to give the idea of movement & international ability
Logo: if you have an idea to adjust the colors, we are open to that. Rosalind likes blues, but other colors didn't seem to work; remember this will print 4c in most cases)
Updates

I have uploaded the logo on it's own. Typical business card size for the US is 3.5" x 2", but doesn't have to be that size. the flyer was just for reference of something else that was done and to give some background. I hope that didn't confuse anyone.

Thank you all for the amazing work in the tight deadline. We will be reviewing everything today and will provide feedback by tomorrow. I will also pass this site on to anyone I know looking for design work.

website address rosalindtavera.example email rosalind@rosalindtavera.example Italian number +39 320 555 0192 USA 1 202 555 0164 International Consulting Services American Know-How. Italian Flair. rtB These are the vital elements for the card. In addition please note the new fotos should have been uploaded. Best Regards

Target Market(s)

Companies or individuals that want to bring the Italian flair to the US or American know how to Italian projects. This can range from a bride planning a destination wedding, an interior designer looking to add pieces or knowledge to their project, or an investor looking to buy property to invest and build.

Industry/Entity Type

Construction

Requirements
Must have
• 1. Company Name with logo: rosalind tavera Enterprises LLC
+39 320 555 0192 (Italia)
Nice to have
• incorporate the idea of international ability; airplanes (like the wing in the background of the logo)
Should not have
• not overly decorative

```html
<!DOCTYPE html>
<html lang="en">
<head>
<meta charset="utf-8">
<title>rosalind tavera Enterprises LLC — Business Card</title>
<link rel="stylesheet" href="https://fonts.googleapis.com/css2?family=Lobster+Two:ital,wght@1,700&family=Roboto+Condensed:wght@400;700&display=swap">
<style>
  :root {
    --bg: #ececec;
    --brand-red: #8a1d14;
    --brand-brown: #5b2b1f;
    --sky-deep: #3f7fc4;
    --sky-mid: #9cc3e8;
    --cloud: #eef3f8;
    --ink-dark: #1d1d1f;
    --white: #ffffff;
    --frame: #bdb5a3;
  }
  * { box-sizing: border-box; margin: 0; padding: 0; }
  html, body { width: 1200px; height: 972px; overflow: hidden; background: var(--bg); }
  .sheet {
    width: 1200px; height: 972px;
    display: flex; flex-direction: column; align-items: center; justify-content: center; gap: 36px;
  }
  .card {
    position: relative; width: 760px; height: 434px; overflow: hidden;
    box-shadow: 0 6px 18px rgba(0,0,0,.18);
  }
  .photo { position: absolute; inset: 0; }
  .photo--wing {
    background: linear-gradient(160deg, var(--sky-deep) 0%, var(--sky-mid) 35%, var(--cloud) 70%, #dfe8f1 100%);
  }
  .photo--window {
    background:
      radial-gradient(ellipse 95% 120% at 40% 55%, transparent 72%, var(--frame) 74%, #6f6a60 82%, #d9d3c6 90%),
      linear-gradient(180deg, #6fa3d8 0%, #cfe1f1 45%, #8aa3bb 62%, #5e7487 100%);
  }
  .front-art { position: absolute; inset: 0; }
  .logo {
    font-family: "Roboto Condensed", sans-serif; font-weight: 400;
    color: var(--brand-brown); display: flex; align-items: center; gap: 10px;
    line-height: 1.15;
  }
  .logo__dot { width: 14px; height: 14px; border-radius: 50%; background: var(--brand-red); flex: none; }
  .front .logo { position: absolute; left: 400px; top: 110px; width: 320px; font-size: 32px; }
  .tagline { position: absolute; text-align: left; }
  .tagline__title {
    font-family: "Lobster Two", cursive; font-style: italic; font-weight: 700;
    font-size: 22px; letter-spacing: .3px;
  }
  .tagline__sub {
    font-family: "Roboto Condensed", sans-serif; font-weight: 700; font-size: 17px;
  }
  .front .tagline { left: 430px; top: 265px; color: var(--brand-red); }
  .back .logo { position: absolute; left: 90px; top: 228px; font-size: 28px; white-space: nowrap; }
  .back .tagline { left: 150px; top: 300px; color: var(--white); }
  .back .tagline__title { font-size: 20px; }
  .back .tagline__sub { font-size: 16px; font-weight: 700; }
  .contact {
    position: absolute; left: 270px; top: 40px; list-style: none;
    font-family: "Roboto Condensed", sans-serif; font-size: 21px; color: var(--ink-dark);
  }
  .contact__item { display: flex; align-items: center; gap: 14px; height: 30px; }
  .contact__icon { width: 20px; height: 20px; flex: none; }
</style>
</head>
<body>
<main class="sheet">

  <section class="card front" aria-label="Business card front">
    <div class="photo photo--wing" role="img" aria-label="Photo of an airplane wing above white clouds and blue sky"></div>
    <svg class="front-art" viewBox="0 0 760 434" aria-hidden="true">
      <path d="M330 0 Q250 260 560 434 L760 434 L760 0 Z" fill="rgba(255,255,255,.55)"/>
      <path d="M330 0 Q250 260 560 434" fill="none" stroke="var(--brand-red)" stroke-width="3"/>
    </svg>
    <div class="logo"><span class="logo__dot"></span><span>rosalind tavera Enterprises LLC</span></div>
    <div class="tagline">
      <p class="tagline__title">International Consulting Services</p>
      <p class="tagline__sub">American Know-How. Italian Flair. rtB</p>
    </div>
  </section>

  <section class="card back" aria-label="Business card back">
    <div class="photo photo--window" role="img" aria-label="Photo through an airplane window showing the wing over land and sky"></div>
    <ul class="contact">
      <li class="contact__item">
        <svg class="contact__icon" viewBox="0 0 20 20"><circle cx="10" cy="10" r="10" fill="var(--brand-red)"/><path d="M10 4a4 4 0 0 0-4 4c0 3 4 8 4 8s4-5 4-8a4 4 0 0 0-4-4z" fill="#fff"/><circle cx="10" cy="8" r="1.5" fill="var(--brand-red)"/></svg>
        Homeport Lucerna Bay, Italy
      </li>
      <li class="contact__item">
        <svg class="contact__icon" viewBox="0 0 20 20"><circle cx="10" cy="10" r="10" fill="var(--brand-red)"/><path d="M7 5l2 2-1 2c1 1.5 2 2.5 3 3l2-1 2 2-1.5 1.5C10 15 5 10 5.5 6.5z" fill="#fff"/></svg>
        +39 320 555 0192 (Italy)
      </li>
      <li class="contact__item">
        <svg class="contact__icon" viewBox="0 0 20 20"><circle cx="10" cy="10" r="10" fill="var(--brand-red)"/><path d="M7 5l2 2-1 2c1 1.5 2 2.5 3 3l2-1 2 2-1.5 1.5C10 15 5 10 5.5 6.5z" fill="#fff"/></svg>
        1 202 555 0164 (USA)
      </li>
      <li class="contact__item">
        <svg class="contact__icon" viewBox="0 0 20 20"><circle cx="10" cy="10" r="10" fill="var(--brand-red)"/><rect x="5" y="6.5" width="10" height="7" fill="#fff"/><path d="M5 6.5l5 4 5-4" fill="none" stroke="var(--brand-red)" stroke-width="1"/></svg>
        rosalind@rosalindtavera.example
      </li>
      <li class="contact__item">
        <svg class="contact__icon" viewBox="0 0 20 20"><circle cx="10" cy="10" r="10" fill="var(--brand-red)"/><circle cx="10" cy="10" r="5" fill="none" stroke="#fff" stroke-width="1.3"/><path d="M5 10h10M10 5c-2 3-2 7 0 10M10 5c2 3 2 7 0 10" fill="none" stroke="#fff" stroke-width="1"/></svg>
        www.rosalindtavera.example
      </li>
    </ul>
    <div class="logo"><span class="logo__dot"></span><span>rosalind tavera Enterprises LLC</span></div>
    <div class="tagline">
      <p class="tagline__title">International Consulting Services</p>
      <p class="tagline__sub">American Know-How. Italian Flair. rtB</p>
    </div>
  </section>

</main>
</body>
</html>
```